Web Site Design for a Finance (lending) Company

We are opening a new subsidiary that focuses on lending money in the real estate industry. We need a web site designed to represent the business.

The business is lending money to real estate investors. A typical client/borrower will be looking to borrow money to buy a house, renovate it and then sell it at a profit, all within 12 months or less.

Company name is Varlo Finance. Our logo is attached.

Attached is a general outline for the web site. We're working on writing more text for each page but this should give you enough to get started with some ideas.

Competitor web site that I like a lot (as an example): https://brixhallfunding.example/. Many of the general items on this site match what we will need (description of loan programs, FAQ)

Target Market(s)

Real estate investors (generally individuals or small companies with just a few people) who are buying homes, renovating them and then selling them at a profit.

Industry/Entity Type

Finance

Coding

Coded - Design and coding required

Number of Pages Required

5+ page

Colors

Designer to choose colors to be used in the design.

Requirements
Must have
• Minimalist design. Clean lines without too much clutter. Some stock photography is ok but the photos should not be distracting. They should almost fade in to the background so that user can focus on the key information about what our company does instead. We are a finance company, not a design company, so the information about our products will be more interesting to site visitors than the art.
• Some minimalist examples from Mosaiko:
• https://www.mosaiko.example/explore/minimalist-web-design/
Nice to have
• If you search in searchly for "hard money lenders" you will find many examples of web sites from our competition. I have provided a link above to competitor web site that I like a lot.
• I have attached our logo in EPS format. Logo is green. Web site doesn't have to be green but it should be of a color that will work well with the logo.

```html
<!DOCTYPE html>
<html lang="en">
<head>
<meta charset="utf-8">
<title>Varlo Finance</title>
<link rel="stylesheet" href="https://fonts.googleapis.com/css2?family=Montserrat:wght@500;600;700&family=Open+Sans:wght@400;600;700&display=swap">
<style>
:root{
  --green:#1d5e3c;
  --green-dark:#154a2e;
  --green-soft:#2b7a4f;
  --ink:#2d2d2d;
  --muted:#6f6f6f;
  --line:#e2e2e2;
  --paper:#ffffff;
  --footer:#3b3b3b;
  --footer-deep:#2a2a2a;
}
*{box-sizing:border-box;margin:0;padding:0}
html,body{width:1200px;height:3380px;overflow:hidden}
body{font-family:"Open Sans",Arial,sans-serif;color:var(--ink);background:var(--paper);font-size:14px;line-height:1.6}
h1,h2,h3,h4{font-family:"Montserrat",Arial,sans-serif}

.topbar{height:32px;background:var(--green-dark);color:#cfe3d6;font-size:12px;display:flex;align-items:center;justify-content:space-between;padding:0 100px}
.header{height:96px;display:flex;align-items:center;padding:0 100px;gap:40px}
.brand{display:flex;align-items:center;gap:12px;font-family:"Montserrat",sans-serif;font-weight:700;font-size:26px;color:var(--green)}
.brand-mark{width:26px;height:26px;background:var(--green)}
.search{margin-left:60px;width:260px;height:38px;border:1px solid var(--line);display:flex;align-items:center;justify-content:space-between;padding:0 12px;color:#aaa;font-size:13px}
.contact-inline{margin-left:auto;display:flex;gap:34px;align-items:center;font-size:15px;color:var(--ink);font-weight:600}
.contact-inline span{display:flex;align-items:center;gap:8px}

.nav{height:52px;background:var(--green);display:flex;align-items:center;padding:0 100px}
.nav a{color:#fff;text-decoration:none;font-family:"Montserrat",sans-serif;font-weight:600;font-size:13px;margin-right:34px;text-transform:uppercase}
.nav .login{margin-left:auto;margin-right:0;background:var(--green-dark);padding:10px 26px;display:flex;gap:8px;align-items:center}

.hero{position:relative;height:520px;background:linear-gradient(180deg,#6f8a6a 0%,#8a7a5a 45%,#c6a86a 70%,#4c6a3e 100%);display:flex;flex-direction:column;align-items:center;justify-content:center;text-align:center}
.hero::before{content:"";position:absolute;inset:0;background:rgba(20,40,28,.35)}
.hero h1{position:relative;color:#fff;font-size:27px;font-weight:600;line-height:1.45;text-transform:uppercase;max-width:820px;margin-top:-150px}
.btn{display:inline-block;background:var(--green);color:#fff;font-family:"Montserrat",sans-serif;font-weight:600;font-size:12px;text-transform:uppercase;padding:11px 22px;text-decoration:none}
.hero .btn{position:relative;margin-top:150px;padding:14px 30px}

.section-title{text-align:center;font-size:28px;font-weight:700;color:var(--ink);text-transform:uppercase}
.title-bar{width:60px;height:4px;background:var(--green);margin:0 auto 14px}
.lead{text-align:center;font-size:13px;color:var(--muted);max-width:820px;margin:10px auto 0}

.about{height:640px;padding-top:60px;position:relative}
.about-body{display:flex;padding:50px 100px 0;gap:60px}
.about-text{width:480px}
.about-text h2{font-size:28px;line-height:1.3;color:var(--ink);font-weight:700}
.about-text h2 b{color:var(--green)}
.about-list{list-style:none;margin-top:30px}
.about-list li{display:flex;gap:30px;font-size:14px;color:#444;margin-bottom:22px}
.about-photo{position:relative;margin-left:40px;margin-top:30px}
.about-photo .frame{position:absolute;left:70px;top:-70px;width:360px;height:400px;border:2px solid var(--green)}
.about-photo .pic{position:relative;width:300px;height:340px;background:linear-gradient(180deg,#b9cfe0 0%,#e6e2d8 40%,#c7c1b2 62%,#5f8a4a 100%)}

.loans{height:840px;background:linear-gradient(160deg,var(--green) 0%,#17503a 100%);padding-top:100px;color:#fff}
.loans .section-title{color:#fff}
.loans .title-bar{background:#fff}
.loans .lead{color:#d6e8dc}
.cards{display:flex;gap:40px;padding:0 140px;margin-top:120px}
.card{position:relative;background:#fff;color:var(--ink);width:440px;height:480px;padding:90px 32px 0}
.card-icon{position:absolute;top:-44px;left:50%;margin-left:-44px;width:88px;height:88px;border-radius:50%;background:var(--green);border:5px solid #fff;display:flex;align-items:center;justify-content:center}
.card h3{font-size:21px;font-weight:700;text-transform:uppercase;text-align:center;border-top:1px solid var(--line);padding-top:26px;margin-bottom:22px}
.card ul{list-style:none}
.card li{display:flex;gap:12px;font-size:12px;color:#555;margin-bottom:16px;line-height:1.5}
.card li::before{content:"";flex:none;width:8px;height:8px;margin-top:5px;border-radius:50%;background:var(--green)}

.blog{height:628px;padding-top:80px}
.posts{display:flex;gap:20px;padding:0 160px;margin-top:50px}
.post{width:280px}
.post .pic{height:200px}
.post h4{font-size:11px;font-weight:700;text-transform:uppercase;margin-top:14px}
.post .meta{display:flex;gap:16px;font-size:10px;color:var(--muted);margin:6px 0}
.post p{font-size:11px;color:#666;line-height:1.5;height:52px}
.post .btn{background:var(--ink);font-size:10px;padding:8px 14px;margin-top:14px}

.newsletter{position:relative;z-index:2;margin:0 100px;height:82px;background:var(--green);display:flex;align-items:center;padding:0 50px;gap:40px}
.newsletter h3{color:#fff;font-size:22px;font-weight:700}
.newsletter .field{width:340px;height:42px;background:#fff;color:#999;font-size:13px;display:flex;align-items:center;padding:0 14px}
.newsletter .btn{height:42px;background:var(--green-dark);padding:0 34px;display:flex;align-items:center;margin-left:-40px}

.footer{margin-top:-10px;height:460px;background:var(--footer);color:#cfcfcf;display:flex;padding:60px 100px 0;gap:60px}
.footer h4{color:#fff;font-size:18px;font-weight:600;margin-bottom:22px}
.footer .col-about{width:240px}
.footer .brand{color:#fff;font-size:22px}
.footer .brand-mark{background:#fff;width:22px;height:22px}
.footer p{font-size:12px;line-height:1.6;margin-top:18px}
.socials{display:flex;gap:12px;margin-top:20px}
.socials span{width:22px;height:22px;border-radius:50%;border:1px solid #9a9a9a}
.col-contact{width:200px}
.contact-row{display:flex;gap:10px;font-size:12px;margin-bottom:16px;align-items:flex-start}
.col-links{width:150px}
.col-links a{display:block;color:#cfcfcf;text-decoration:none;font-size:12px;margin-bottom:12px}
.col-form{width:220px}
.input{height:32px;background:#4a4a4a;border:1px solid #5a5a5a;color:#9a9a9a;font-size:11px;display:flex;align-items:center;padding:0 10px;margin-bottom:10px}
.input.tall{height:80px;align-items:flex-start;padding-top:8px}
.col-form .btn{display:block;text-align:center;font-size:14px;padding:10px 0;margin-top:10px}
.bottombar{height:40px;background:var(--footer-deep);color:#aaa;font-size:11px;display:flex;align-items:center;justify-content:center}
</style>
</head>
<body>

<div class="topbar">
  <span>info@varlofinance.example</span>
  <span>Mon – Fri: 9:00 – 18:00</span>
</div>

<header class="header">
  <div class="brand"><span class="brand-mark"></span>Varlo Finance</div>
  <div class="search">Search
    <svg width="14" height="14" viewBox="0 0 14 14"><circle cx="6" cy="6" r="4.5" fill="none" stroke="#999" stroke-width="1.5"/><line x1="9.5" y1="9.5" x2="13" y2="13" stroke="#999" stroke-width="1.5"/></svg>
  </div>
  <div class="contact-inline">
    <span><svg width="18" height="18" viewBox="0 0 24 24"><path d="M6.6 10.8a15 15 0 0 0 6.6 6.6l2.2-2.2a1 1 0 0 1 1-.25 11.4 11.4 0 0 0 3.6.6 1 1 0 0 1 1 1V20a1 1 0 0 1-1 1A17 17 0 0 1 3 4a1 1 0 0 1 1-1h3.5a1 1 0 0 1 1 1c0 1.25.2 2.45.6 3.6a1 1 0 0 1-.25 1z" fill="#1d5e3c"/></svg>(555) 014-2290</span>
    <span><svg width="18" height="14" viewBox="0 0 18 14"><rect x="1" y="1" width="16" height="12" fill="none" stroke="#1d5e3c" stroke-width="1.6"/><path d="M1 1l8 7 8-7" fill="none" stroke="#1d5e3c" stroke-width="1.6"/></svg>info@varlofinance.example</span>
  </div>
</header>

<nav class="nav">
  <a href="#">Home</a><a href="#">About Us</a><a href="#">Loan Programs ▾</a><a href="#">Partners</a><a href="#">Contact</a><a href="#">Apply Now</a>
  <a href="#" class="login"><svg width="12" height="12" viewBox="0 0 12 12"><circle cx="6" cy="4" r="2.5" fill="#fff"/><path d="M1 12a5 5 0 0 1 10 0z" fill="#fff"/></svg>Login</a>
</nav>

<section class="hero" role="img" aria-label="Photo of a two-storey suburban house with a front lawn and trees">
  <h1>Varlo has an established pool of experienced investors available for your real estate investment needs</h1>
  <a href="#" class="btn">Read More</a>
</section>

<section class="about">
  <div class="title-bar"></div>
  <h2 class="section-title">About Us</h2>
  <div class="about-body">
    <div class="about-text">
      <h2>Specializing in housing and offices, <b>VARLO FINANCE</b> has a wide range of activities</h2>
      <ol class="about-list">
        <li><span>1</span>Project management administrative management/acquisition.</li>
        <li><span>2</span>Development and upgrading of urban areas</li>
        <li><span>3</span>Promotion and sale</li>
        <li><span>4</span>In housing and offices, promotion and sale</li>
      </ol>
    </div>
    <div class="about-photo">
      <div class="frame"></div>
      <div class="pic" role="img" aria-label="Photo of a white family house with a porch and green lawn"></div>
    </div>
  </div>
</section>

<section class="loans">
  <div class="title-bar"></div>
  <h2 class="section-title">Our Loans Plans</h2>
  <p class="lead">Clear terms and fast decisions for investors who buy, renovate and sell homes. Pick the plan that fits your next project and apply online in minutes.</p>
  <div class="cards">
    <article class="card">
      <div class="card-icon"><svg width="40" height="40" viewBox="0 0 40 40"><path d="M15 8h10l-3 6h-4z" fill="#fff"/><path d="M17 14h6c6 4 10 10 10 15a7 7 0 0 1-7 7H14a7 7 0 0 1-7-7c0-5 4-11 10-15z" fill="#fff"/><text x="20" y="31" text-anchor="middle" font-family="Montserrat,sans-serif" font-weight="700" font-size="12" fill="#1d5e3c">$</text></svg></div>
      <h3>Fix and Flip Loans</h3>
      <ul>
        <li>Description of the loan type, borrower requirements</li>
        <li>Short term funding for buying and renovating a home, repaid once the property is sold within twelve months.</li>
        <li>Why choose Varlo</li>
        <li>Apply online or contact our team to get your quote and approval, with funds ready to close on your timeline.</li>
      </ul>
    </article>
    <article class="card">
      <div class="card-icon"><svg width="44" height="30" viewBox="0 0 44 30"><rect x="2" y="4" width="40" height="22" rx="2" fill="none" stroke="#fff" stroke-width="2.5"/><circle cx="22" cy="15" r="6" fill="none" stroke="#fff" stroke-width="2"/><circle cx="9" cy="15" r="2" fill="#fff"/><circle cx="35" cy="15" r="2" fill="#fff"/></svg></div>
      <h3>Commercial Hard Money Loans</h3>
      <ul>
        <li>Description of the loan type, borrower requirements</li>
        <li>Asset based loans for offices and mixed use buildings, with terms set around your plans for the property.</li>
        <li>Why choose Varlo</li>
        <li>Apply online or contact our team to get your quote and approval, with funds ready to close on your timeline.</li>
      </ul>
    </article>
  </div>
</section>

<section class="blog">
  <div class="title-bar"></div>
  <h2 class="section-title">Latest Blog</h2>
  <p class="lead">News, market notes and practical tips for real estate investors planning their next purchase and renovation.</p>
  <div class="posts">
    <article class="post">
      <div class="pic" role="img" aria-label="Photo of glass office towers against a blue sky" style="background:linear-gradient(160deg,#1d5fa8,#7fb6e6 60%,#d6ecfb)"></div>
      <h4>How to value a flip property</h4>
      <div class="meta"><span>Admin</span><span>12 Aug 2017</span><span>4 min</span></div>
      <p>A simple method to estimate repair costs and resale value before you make an offer on a home.</p>
      <a href="#" class="btn">Read More</a>
    </article>
    <article class="post">
      <div class="pic" role="img" aria-label="Photo of a hand holding a house key with a red keyring" style="background:linear-gradient(160deg,#e9e9e9,#bdbdbd 60%,#8a2a2a)"></div>
      <h4>Closing faster on your next deal</h4>
      <div class="meta"><span>Admin</span><span>09 Aug 2017</span><span>3 min</span></div>
      <p>The papers to prepare early so your loan can be approved and funded in days, not weeks.</p>
      <a href="#" class="btn">Read More</a>
    </article>
    <article class="post">
      <div class="pic" role="img" aria-label="Photo of a hand placing a coin beside a small model house and a plant" style="background:linear-gradient(160deg,#f1ede4,#c9b98f 55%,#4f7a3a)"></div>
      <h4>Budgeting a home renovation</h4>
      <div class="meta"><span>Admin</span><span>02 Aug 2017</span><span>5 min</span></div>
      <p>Where to spend and where to save when updating a house you plan to sell within the year.</p>
      <a href="#" class="btn">Read More</a>
    </article>
  </div>
</section>

<section class="newsletter">
  <h3>Subscribe to our newsletter</h3>
  <div class="field">Email Address</div>
  <a href="#" class="btn">Subscribe</a>
</section>

<footer class="footer">
  <div class="col-about">
    <div class="brand"><span class="brand-mark"></span>Varlo Finance</div>
    <p>Short term loans for investors who buy, renovate and sell homes. Fast answers, clear terms and a team that knows local real estate.</p>
    <div class="socials"><span></span><span></span><span></span><span></span><span></span></div>
  </div>
  <div class="col-contact">
    <h4>Contact Us</h4>
    <div class="contact-row"><svg width="12" height="16" viewBox="0 0 12 16"><path d="M6 0a6 6 0 0 1 6 6c0 4-6 10-6 10S0 10 0 6a6 6 0 0 1 6-6z" fill="#cfcfcf"/><circle cx="6" cy="6" r="2" fill="#3b3b3b"/></svg>410 Harlow Street, Suite 8, Fairview</div>
    <div class="contact-row"><svg width="14" height="14" viewBox="0 0 24 24"><path d="M6.6 10.8a15 15 0 0 0 6.6 6.6l2.2-2.2a1 1 0 0 1 1-.25 11.4 11.4 0 0 0 3.6.6 1 1 0 0 1 1 1V20a1 1 0 0 1-1 1A17 17 0 0 1 3 4a1 1 0 0 1 1-1h3.5a1 1 0 0 1 1 1c0 1.25.2 2.45.6 3.6a1 1 0 0 1-.25 1z" fill="#cfcfcf"/></svg>(555) 014-2290</div>
    <div class="contact-row"><svg width="14" height="11" viewBox="0 0 18 14"><rect x="1" y="1" width="16" height="12" fill="none" stroke="#cfcfcf" stroke-width="1.6"/><path d="M1 1l8 7 8-7" fill="none" stroke="#cfcfcf" stroke-width="1.6"/></svg>info@varlofinance.example</div>
  </div>
  <div class="col-links">
    <h4>Useful Links</h4>
    <a href="#">About Us</a><a href="#">Loan Programs</a><a href="#">Careers &amp; Staff</a><a href="#">Contact Us</a><a href="#">Privacy Policy</a>
  </div>
  <div class="col-form">
    <h4>Get in Touch</h4>
    <div class="input">Your Name</div>
    <div class="input">Your Email</div>
    <div class="input tall">Your Message</div>
    <a href="#" class="btn">Send</a>
  </div>
</footer>

<div class="bottombar">© 2017 Varlo Finance. All Rights Reserved</div>

</body>
</html>
```